Marigold Cleaning Service LTD its all about cleaning ( Domestic Cleaning, Commercial Cleaning, Student Accommodations, Corridors, Halls & Common Areas). I'm looking for POSH/ ELEGANT LOOKING design of flyers, which presents all Services we provide, it also should include 5% discount for new customers, contact details: website: www.marigold-clean.example.co.uk email address: marigoldservice@mailbox-example.com Mobile phone no: 07700900417 and home no: 01632960582 . I would like to include logo of the company, without any pictures of buckets etc.(that in my opinion pictures like that looks "cheap"). It should be design which perfectly match logo of the company, I would like also to include slogan of Marigold "You Deserve Marigold Cleaners". I was thinking to make those flyers, bright "clean" (maybe background could be beige color, on the other hand I think Navy color looks elegant as well, I'm looking for something posh NOT like some random cleaning company, It should be something UNIQUE). Of course by this flyers Marigold Cleaning Service should increase profits. If you will have any draft or any questions please contact me at any time on email: h.walters@mailbox-example.com or by phone: 07700900417
Best Regards
Hilda Walters
Marigold Cleaning Service LTD

```html
<!DOCTYPE html>
<html lang="en">
<head>
<meta charset="utf-8">
<title>Marigold Cleaning Service LTD – Flyer</title>
<link rel="stylesheet" href="https://fonts.googleapis.com/css2?family=Arimo:wght@400;700&family=Tinos:wght@400&display=swap">
<style>
  :root {
    --frame-blue: #0db1ec;
    --bright-cyan: #19b8f0;
    --cyan-shadow: #0a5fa8;
    --beige: #fdf1d9;
    --white: #ffffff;
    --navy: #0f2b46;
    --royal: #1d4f9c;
    --ink-blue: #1a3f8a;
  }
  * { margin: 0; padding: 0; box-sizing: border-box; }
  html, body {
    width: 1200px;
    height: 844px;
    overflow: hidden;
    background: var(--white);
  }
  .flyer {
    position: relative;
    width: 1200px;
    height: 844px;
    background: var(--white);
    border: 16px solid var(--frame-blue);
    overflow: hidden;
  }
  .backdrop {
    position: absolute;
    left: 0; top: 0;
    width: 1168px; height: 812px;
  }

  .offer-figure {
    position: absolute;
    left: 173px;
    top: -4px;
    font-family: "Arimo", Arial, sans-serif;
    font-weight: 400;
    font-size: 165px;
    line-height: 1;
    color: var(--bright-cyan);
    text-shadow: 3px 3px 0 var(--cyan-shadow);
    letter-spacing: -3px;
    white-space: nowrap;
  }
  .offer-note {
    font-family: "Tinos", "Times New Roman", serif;
    font-size: 34px;
    line-height: 1;
    color: var(--ink-blue);
    white-space: nowrap;
  }
  .offer-note .line1 { position: absolute; left: 263px; top: 145px; }
  .offer-note .line2 { position: absolute; left: 251px; top: 175px; }

  .brand-frame {
    position: absolute;
    left: 496px;
    top: 2px;
    width: 674px;
    height: 451px;
    background: var(--beige);
    padding: 14px 16px 20px 15px;
  }
  .brand-panel {
    width: 100%;
    height: 100%;
    background: var(--white);
    position: relative;
  }
  .brand-name {
    font-family: "Arimo", Arial, sans-serif;
    font-weight: 400;
    color: var(--navy);
    line-height: 1;
  }
  .brand-name .first {
    position: absolute;
    left: 90px;
    top: 176px;
    font-size: 80px;
    white-space: nowrap;
  }
  .brand-name .rest {
    position: absolute;
    left: 14px;
    top: 294px;
    font-size: 56px;
    white-space: nowrap;
  }

  .contact {
    position: absolute;
    left: 24px;
    top: 406px;
    font-family: "Arimo", Arial, sans-serif;
    font-weight: 700;
    font-size: 17px;
    line-height: 21px;
    color: var(--royal);
    list-style: none;
  }
  .contact li:first-child { padding-left: 6px; }

  .services {
    position: absolute;
    left: 437px;
    top: 486px;
    width: 727px;
    font-family: "Tinos", "Times New Roman", serif;
    font-size: 23px;
    line-height: 34px;
    color: var(--ink-blue);
    text-align: center;
    list-style: none;
  }
  .services li { display: inline; white-space: nowrap; }
  .services li + li::before { content: "\00B7"; padding: 0 10px; color: var(--bright-cyan); }
  .services li.break-before::before { content: ""; padding: 0; }
  .services li.break-before { display: block; }

  .slogan {
    position: absolute;
    left: 436px;
    top: 614px;
    font-family: "Tinos", "Times New Roman", serif;
    font-size: 51px;
    line-height: 1.15;
    color: var(--ink-blue);
    white-space: nowrap;
  }
</style>
</head>
<body>
  <main class="flyer">
    <svg class="backdrop" viewBox="0 0 1168 812" aria-hidden="true">
      <polygon points="0,0 500,456 0,812" fill="var(--beige)"/>
    </svg>

    <span class="offer-figure">5%</span>
    <p class="offer-note">
      <span class="line1">discount for</span>
      <span class="line2">new customers</span>
    </p>

    <div class="brand-frame">
      <div class="brand-panel">
        <h1 class="brand-name">
          <span class="first">Marigold</span>
          <span class="rest">Cleaning Service LTD</span>
        </h1>
      </div>
    </div>

    <ul class="contact">
      <li>www.marigold-clean.example.co.uk</li>
      <li>Email address: marigoldservice@mailbox-example.com</li>
      <li>Mobile phone no: 07700900417</li>
      <li>Home no: 01632960582 .</li>
    </ul>

    <ul class="services">
      <li>Domestic Cleaning</li>
      <li>Commercial Cleaning</li>
      <li>Student Accommodations</li>
      <li class="break-before">Corridors, Halls &amp; Common Areas</li>
    </ul>

    <p class="slogan">“You Deserve Marigold Cleaners"</p>
  </main>
</body>
</html>
```